Business card for Drone Aerial

I need a business card designed keeping in mind I want to do post cards also with a similar design.
Both sides of the card would be cool.
I have a vortel 8 max and would like a picture of it on the front of the card. Similar to one I attached.
I really like the look of a drone in the air and the background pic a little blurry. I attached a few images as IDEAS.
Some special things I want to be on the card additional to the normal business card info:
"Aerial Photography" or "Low Altitude Aerial Photography"?
"KTO# 58203917"

I like modern and creative. My Favorite color is blue and I like blue on white.
I do not have a business name and am not going to have one. When they read "Aerial Photography" and see the drone and image they will know what the card is for.

FYI, The attached pictures are just images from pixelgrove and just samples/ideas.

Target Market(s)

Real estate, construction, events

Industry/Entity Type

Business

Contact Information for Business Card

Also Definitely want to contain, my name, my number and email address.

Requirements
Must have
• "KTO# 58203917"
• "Aerial Photography"

```html
<!DOCTYPE html>
<html lang="en">
<head>
<meta charset="utf-8">
<title>Aerial Photography – Business Card</title>
<link href="https://fonts.googleapis.com/css2?family=Open+Sans:wght@400;600&display=swap" rel="stylesheet">
<style>
  :root {
    --page-bg: #eceef1;
    --brand-blue: #1a5aab;
    --brand-blue-deep: #0d4a9c;
    --brand-blue-light: #2f74c6;
    --card-white: #ffffff;
    --text-grey: #6f7a86;
    --shadow: rgba(20, 40, 70, 0.18);
  }
  * { margin: 0; padding: 0; box-sizing: border-box; }
  html, body { width: 1200px; height: 1023px; overflow: hidden; }
  body {
    background: var(--page-bg);
    font-family: "Open Sans", Arial, sans-serif;
    position: relative;
  }
  .card {
    position: absolute;
    width: 540px;
    height: 310px;
    border-radius: 4px;
    overflow: hidden;
    box-shadow: 0 10px 28px var(--shadow);
  }
  .card--front { left: 45px; top: 356px; background: var(--card-white); }
  .card--back {
    left: 615px; top: 356px;
    background: linear-gradient(160deg, var(--brand-blue-light) 0%, var(--brand-blue-deep) 70%);
  }
  .front-art { position: absolute; inset: 0; }
  .brand {
    position: absolute;
    left: 36px; top: 150px;
    display: flex; align-items: center; gap: 12px;
  }
  .brand__mark {
    width: 54px; height: 54px; border-radius: 50%;
    background: var(--brand-blue);
  }
  .brand__name {
    font-size: 25px; font-weight: 600; letter-spacing: 0.5px;
    color: var(--brand-blue); text-transform: uppercase;
  }
  .person { position: absolute; left: 102px; top: 208px; }
  .person__name { font-size: 19px; font-weight: 600; color: var(--brand-blue); line-height: 1.15; }
  .person__role { font-size: 11px; color: var(--text-grey); line-height: 14px; }
  .contact { position: absolute; left: 102px; top: 246px; font-size: 11px; color: var(--text-grey); }
  .contact__row { display: flex; align-items: center; gap: 6px; line-height: 16px; }
  .contact__icon { width: 11px; height: 11px; fill: var(--brand-blue); }
  .address {
    position: absolute; right: 26px; top: 64px;
    text-align: right; font-size: 12px; line-height: 16px; color: var(--text-grey);
  }
  .address__licence { font-weight: 600; color: var(--brand-blue); }
  .back-brand {
    position: absolute; inset: 0;
    display: flex; align-items: center; justify-content: center; gap: 22px;
  }
  .back-brand__name {
    font-size: 28px; font-weight: 600; letter-spacing: 1px;
    color: var(--card-white); text-transform: uppercase;
  }
  .back-brand__mark {
    width: 110px; height: 110px; border-radius: 50%;
    background: var(--card-white);
  }
</style>
</head>
<body>

<section class="card card--front">
  <svg class="front-art" width="540" height="310" viewBox="0 0 540 310">
    <defs>
      <linearGradient id="skyPhoto" x1="0" y1="0" x2="0" y2="1">
        <stop offset="0" stop-color="#9fbfe0"/>
        <stop offset="1" stop-color="#d6e4f2"/>
      </linearGradient>
    </defs>
    <g role="img" aria-label="Blurred photo of a drone flying in a blue sky">
      <path d="M0,0 H540 V28 Q300,58 0,135 Z" fill="url(#skyPhoto)"/>
    </g>
    <path d="M0,135 Q300,58 540,28 V40 Q300,72 0,150 Z" fill="var(--brand-blue)"/>
    <path d="M0,292 V310 H540 V306 Q260,312 0,292 Z" fill="var(--brand-blue)"/>
  </svg>

  <div class="brand">
    <span class="brand__mark"></span>
    <span class="brand__name">Aerial Photography</span>
  </div>

  <div class="person">
    <div class="person__name">Maren Tolliver</div>
    <div class="person__role">Director</div>
  </div>

  <div class="contact">
    <div class="contact__row">
      <svg class="contact__icon" viewBox="0 0 24 24"><path d="M6.6 10.8a15.1 15.1 0 0 0 6.6 6.6l2.2-2.2a1 1 0 0 1 1-.25 11.4 11.4 0 0 0 3.6.57 1 1 0 0 1 1 1V20a1 1 0 0 1-1 1A17 17 0 0 1 3 4a1 1 0 0 1 1-1h3.5a1 1 0 0 1 1 1c0 1.25.2 2.45.57 3.57a1 1 0 0 1-.25 1z"/></svg>
      <span>0487 204 316</span>
    </div>
    <div class="contact__row">
      <svg class="contact__icon" viewBox="0 0 24 24"><path d="M2 5h20v14H2z M3 6l9 7 9-7" stroke="#fff" stroke-width="1.5"/></svg>
      <span>maren@skyframestudio.com.au</span>
    </div>
  </div>

  <div class="address">
    Consulting Rooms<br>
    52 Larchmont Street<br>
    Kewdale VIC 3188<br>
    <span class="address__licence">KTO# 58203917</span>
  </div>
</section>

<section class="card card--back">
  <div class="back-brand">
    <span class="back-brand__name">Aerial Photography</span>
    <span class="back-brand__mark"></span>
  </div>
</section>

</body>
</html>
```